Brochure Design Project

We are a manufacturing business based in Archerfield, Australia. We service the air conditioning industry. Our brochure will have some of our information and history on one side, followed by a list of products and services on the back.

Our current logo must be used.

Size will be

216mm x 279mm

Double sided.

Target Market(s)

air conditioning contractors

Industry/Entity Type

Air Conditioning

Requirements
Must have
• Must haves

Company history paragraph

Torvel Insulation Has been established in the HVAC industry since 1984. It has grown from 2 to 16 employees.

We pride ourselves on offering the fastest lagging service in Brisbane. With our new CNC machine we can meet any demands large or small.

services-
Internal and external insulating of HVAC ductwork
Manufacture of metal cushion boxes
Manufacture of ductboard cushion boxes
Cut and facing of insulation to size and shape.

Products-
glasswool insulation
ductboard
Closed cell foam
Baffloro
Ceramic board
variety of foils
metal spigots
pins and clips

Pictures of our products

Factory location-
47 Mardlow Street
Archerfield, QLD, 4152

Telephone number-
07 3519 0264

Email address-
mark@torvelinsulation.com.au

```html
<!DOCTYPE html>
<html lang="en">
<head>
<meta charset="utf-8">
<title>Torvel Insulation – Services and Products</title>
<link rel="stylesheet" href="https://fonts.googleapis.com/css2?family=Roboto+Slab:wght@700;800&display=swap">
<style>
  :root {
    --ribbon-brown: #b0552b;
    --ribbon-orange: #e8692e;
    --tab-orange: #e66a30;
    --paper: #ffffff;
    --ink: #1c1a19;
    --star: #b8693f;
    --photo-ducts: #b7bcc2;
    --photo-boards: #8f8880;
    --photo-workshop: #a99b89;
    --photo-pins: #c9c8d6;
  }
  * { margin: 0; padding: 0; box-sizing: border-box; }
  html, body { width: 932px; height: 1200px; overflow: hidden; background: var(--paper); }
  .sheet { position: relative; width: 932px; height: 1200px; overflow: hidden; background: var(--paper); }
  .backdrop { position: absolute; inset: 0; }
  .section-tab {
    position: absolute; left: 0; height: 46px; width: 290px;
    background: var(--tab-orange);
    clip-path: polygon(0 0, 205px 0, 290px 100%, 0 100%);
  }
  .section-title {
    position: absolute; left: 50px;
    font-family: "Roboto Slab", serif; font-weight: 800; font-size: 30px;
    color: var(--ink); line-height: 46px; white-space: nowrap;
  }
  .tab-services, .title-services { top: 284px; }
  .tab-products, .title-products { top: 538px; }
  .item-list {
    position: absolute; list-style: none;
    font-family: "Roboto Slab", serif; font-weight: 700; font-size: 17px;
    letter-spacing: 0.2px; color: var(--ink); white-space: nowrap;
  }
  .item-list li { position: relative; padding-left: 26px; height: 37.5px; line-height: 22px; }
  .item-list li::before { content: "\2606"; position: absolute; left: 0; top: 0; color: var(--star); font-size: 15px; font-weight: 400; }
  .services-list { left: 128px; top: 355px; }
  .products-list { top: 610px; }
  .products-col-1 { left: 128px; }
  .products-col-2 { left: 356px; }
  .products-col-3 { left: 643px; }
</style>
</head>
<body>
<main class="sheet">
  <svg class="backdrop" width="932" height="1200" viewBox="0 0 932 1200">
    <defs>
      <linearGradient id="metalTone" x1="0" y1="0" x2="1" y2="1">
        <stop offset="0" stop-color="#6f757b"/><stop offset="0.5" stop-color="#b3b8bd"/><stop offset="1" stop-color="#7a7f85"/>
      </linearGradient>
      <linearGradient id="woolTone" x1="0" y1="0" x2="0" y2="1">
        <stop offset="0" stop-color="#efe04e"/><stop offset="1" stop-color="#d8bf2e"/>
      </linearGradient>
    </defs>
    <rect x="0" y="0" width="292" height="330" fill="var(--photo-ducts)" role="img" aria-label="Galvanised duct plenum boxes fitted with round metal spigots"/>
    <rect x="292" y="0" width="346" height="330" fill="var(--photo-boards)" role="img" aria-label="Stacked insulation boards in the factory"/>
    <rect x="638" y="0" width="294" height="560" fill="var(--photo-workshop)" role="img" aria-label="Worker assembling an insulated cushion box in the workshop"/>
    <rect x="0" y="700" width="322" height="500" fill="url(#metalTone)" role="img" aria-label="Close-up of perforated metal sheet"/>
    <rect x="322" y="860" width="323" height="340" fill="var(--photo-pins)" role="img" aria-label="Insulation pins with perforated base plates and clips"/>
    <rect x="645" y="900" width="287" height="300" fill="url(#woolTone)" role="img" aria-label="Stack of yellow glasswool insulation batts"/>

    <path d="M0,75 C110,235 360,225 600,275 C800,320 915,380 932,560 L932,1000 C860,920 650,890 420,850 C200,810 20,760 0,650 Z" fill="var(--paper)"/>

    <path d="M0,0 L22,0 C130,160 380,170 620,225 C820,272 932,300 932,330 L932,560 C915,380 800,320 600,275 C360,225 110,235 0,75 Z" fill="var(--ribbon-brown)"/>
    <path d="M0,28 C118,192 372,196 612,249 C812,296 926,345 932,450" fill="none" stroke="var(--ribbon-orange)" stroke-width="17"/>

    <path d="M0,650 C20,760 200,810 420,850 C650,890 860,920 932,1000 L932,1100 C870,990 700,960 500,935 C300,910 150,880 0,830 Z" fill="var(--ribbon-brown)"/>
    <path d="M0,705 C60,810 230,850 450,885 C670,915 870,945 932,1035" fill="none" stroke="var(--ribbon-orange)" stroke-width="18"/>
  </svg>

  <div class="section-tab tab-services"></div>
  <h2 class="section-title title-services">Services</h2>
  <ul class="item-list services-list">
    <li>Internal and external insulating of HVAC ductwork</li>
    <li>Manufacture of metal cushion boxes</li>
    <li>Manufacture of ductboard cushion boxes</li>
    <li>Cut and facing of insulation to size and shape.</li>
  </ul>

  <div class="section-tab tab-products"></div>
  <h2 class="section-title title-products">Products</h2>
  <ul class="item-list products-list products-col-1">
    <li>Glasswool</li>
    <li>Insulation</li>
    <li>Ductboard</li>
  </ul>
  <ul class="item-list products-list products-col-2">
    <li>Closed cell foam</li>
    <li>Baffloro</li>
    <li>Ceramic Board</li>
  </ul>
  <ul class="item-list products-list products-col-3">
    <li>Variety of Foils</li>
    <li>Metal Spigots</li>
    <li>Pins and Clips</li>
  </ul>
</main>
</body>
</html>
```